Tovrel Business Card

We are a modern retail clothing store. Established in 1994. I need a presentable card that will amaze vendors when given to them.

Front: Logo in middle
Info Side:

Name: Omar Latif
Cell: 630-555-0148
Work: 630-555-0192 EXT. 230
Email: Omar@tovrel.example
Website: www.Tovrel.example

Industry/Entity Type

Business

```html
<!DOCTYPE html>
<html lang="en">
<head>
<meta charset="utf-8">
<title>Tovrel Business Card</title>
<link rel="stylesheet" href="https://fonts.googleapis.com/css2?family=Oswald:wght@500&family=Open+Sans:wght@400&display=swap">
<style>
  :root {
    --page: #e9e7e4;
    --card: #232323;
    --ink: #ffffff;
    --ink-soft: #e6e6e6;
    --mark: #3b3b3b;
  }
  * { margin: 0; padding: 0; box-sizing: border-box; }
  html, body { width: 1200px; height: 1000px; overflow: hidden; }
  body { background: var(--page); position: relative; font-family: "Open Sans", Arial, sans-serif; }

  .card {
    position: absolute;
    left: 265px;
    width: 665px;
    height: 397px;
    background: var(--card);
    border-radius: 22px;
  }
  .card--info { top: 73px; }
  .card--brand { top: 532px; }

  .identity {
    position: absolute;
    right: 352px;
    top: 160px;
    text-align: right;
    color: var(--ink);
  }
  .identity__name {
    font-family: "Oswald", "Arial Narrow", sans-serif;
    font-weight: 500;
    font-size: 37px;
    line-height: 46px;
    letter-spacing: 0.2px;
    text-transform: uppercase;
  }
  .identity__title {
    font-size: 15px;
    line-height: 20px;
    color: var(--ink-soft);
  }

  .divider {
    position: absolute;
    left: 332px;
    top: 155px;
    width: 2px;
    height: 88px;
    background: var(--ink);
  }

  .contacts {
    position: absolute;
    left: 352px;
    top: 152px;
    list-style: none;
    color: var(--ink-soft);
    font-size: 15.5px;
  }
  .contacts__item {
    display: flex;
    align-items: center;
    height: 23.5px;
  }
  .contacts__icon {
    width: 14px;
    height: 14px;
    margin-right: 8px;
    fill: var(--ink-soft);
    flex: none;
  }

  .brand {
    position: absolute;
    left: 0;
    right: 0;
    top: 118px;
    text-align: center;
    font-family: "Oswald", "Arial Narrow", sans-serif;
    font-weight: 500;
    font-size: 112px;
    line-height: 140px;
    letter-spacing: 4px;
    text-transform: uppercase;
    color: var(--mark);
  }
</style>
</head>
<body>

<section class="card card--info" aria-label="Contact side">
  <div class="identity">
    <div class="identity__name">Omar Latif</div>
    <div class="identity__title">Vice President</div>
  </div>
  <div class="divider"></div>
  <ul class="contacts">
    <li class="contacts__item">
      <svg class="contacts__icon" viewBox="0 0 14 14" aria-hidden="true"><path d="M4 1h6a1 1 0 0 1 1 1v10a1 1 0 0 1-1 1H4a1 1 0 0 1-1-1V2a1 1 0 0 1 1-1zm.5 1.5v6h5v-6zM6 10.5h2v1H6z"/></svg>
      630-555-0148
    </li>
    <li class="contacts__item">
      <svg class="contacts__icon" viewBox="0 0 14 14" aria-hidden="true"><path d="M1 5c0-2 3-3 6-3s6 1 6 3v1h-3V4.5H4V6H1zM3 7h8l1.5 5h-11zm4 1.2a1.6 1.6 0 1 0 0 3.2 1.6 1.6 0 0 0 0-3.2z"/></svg>
      630-555-0192 EXT. 230
    </li>
    <li class="contacts__item">
      <svg class="contacts__icon" viewBox="0 0 14 14" aria-hidden="true"><path d="M1 3h12v8H1zm1.2 1.2v.3L7 7.6l4.8-3.1v-.3zm0 1.7v4h9.6v-4L7 9z"/></svg>
      Omar@tovrel.example
    </li>
    <li class="contacts__item">
      <svg class="contacts__icon" viewBox="0 0 14 14" aria-hidden="true"><path d="M7 1a6 6 0 1 0 0 12A6 6 0 0 0 7 1zm0 1.3c.8.8 1.3 2 1.5 3.2h-3C5.7 4.3 6.2 3.1 7 2.3zM2.4 7a4.6 4.6 0 0 1 .2-1.5h1.6A9 9 0 0 0 4.2 8H2.5zm3.1 1.5h3c-.2 1.2-.7 2.4-1.5 3.2-.8-.8-1.3-2-1.5-3.2zm4.3 0h1.7a4.6 4.6 0 0 1-2.5 2.8c.4-.8.7-1.8.8-2.8zm0-3h1.6a4.6 4.6 0 0 1 .1 2.2H9.8a9 9 0 0 0 0-2.2z"/></svg>
      www.Tovrel.example
    </li>
  </ul>
</section>

<section class="card card--brand" aria-label="Brand side">
  <div class="brand">Tovrel</div>
</section>

</body>
</html>
```